Auction Company Wordpress Design Project

We need a WordPress design/concept for an established auctioneering company specializing in Benefit Auctions, Estate Auctions, Business Liquidations/Overstocks, and real estate marketing in the Chicago area. The winning design will have a professional look appealing to clients searching for these services.

Industry/Entity Type

Real Estate

Requirements
Must have
• - We will require winning designer to provide a layered PSD (Adobe photoshop) concept file, along with any non-standard font files used.

The site's navigation: 1) Home, 2) Auctions, 3) About Us, 4) Buyers, 5) Sellers, 6) Media, 7) Contact Us. Horizontal structure preferred.

A slideshow element will be represented (choice of files attached) preferably in the header. The following widgets will also be incorporated into sidebar (or other creative placement):
- Steady Relay email signup
- Featured Auctions (example shown in http://www.bidplainfield.example/ as "Upcoming Auctions" widget)
- Clipvane video widget
- Social media widget for Pallroom, Chirble, Clipvane icons
- Testimonials widget

Winning design will creatively use colors in logo (with perhaps accent color) with a professional, clean look. Client mentions liking the use of color in http://www.lotvistara.example/

Footer of site will have generic contact info (phone number, email addresses, mailing address; a smaller instance of logo; and the attached association logos.
Nice to have
• - Use of drop-down menus should be demonstrated by incorporating mouse-over for 1) Upcoming, 2) Online, 3) Past, under the 'Auctions' main menu item (for clarity of design, this drop-down can be placed under any other menu item if necessary).
Should not have
• Please do not use auction gavels in the design.

```html
<!DOCTYPE html>
<html lang="en">
<head>
<meta charset="utf-8">
<title>Harvest Gate Auctions</title>
<link rel="stylesheet" href="https://fonts.googleapis.com/css2?family=Arimo:wght@400;700&family=Source+Sans+3:wght@400;600&family=Tinos&display=swap">
<style>
:root{
  --tan:#d8cba2;
  --tan-dark:#b9a57a;
  --gold:#a8925f;
  --beige:#efe8d3;
  --ink:#1f1f1f;
  --footer:#383b3e;
  --green-top:#8cbc2a;
  --green-bot:#5e9612;
  --line:#d9d9d9;
}
*{margin:0;padding:0;box-sizing:border-box}
html,body{width:1200px;height:1183px;overflow:hidden;background:#fff}
body{position:relative;font-family:"Arimo",Arial,sans-serif;color:var(--ink)}
.top-stripe{position:absolute;left:0;top:0;width:1200px;height:6px;background:var(--tan)}
.header{position:absolute;left:0;top:6px;width:1200px;height:113px;background:#fff}
.brand{position:absolute;left:118px;top:0;width:123px;height:186px;z-index:5}
.brand svg{position:absolute;left:0;top:0}
.brand-name{position:absolute;left:8px;top:58px;width:107px;text-align:center;font-family:"Source Sans 3",sans-serif;font-weight:600;font-size:19px;line-height:21px;color:#2a2620}
.nav{position:absolute;left:380px;top:69px;display:flex;list-style:none}
.nav li{position:relative;height:30px;line-height:30px;font-size:15px;color:#222}
.nav li+li::before{content:"";position:absolute;left:0;top:3px;height:24px;border-left:1px solid var(--line)}
.nav .home{background:var(--tan);padding:0 10px;width:61px}
.nav .auctions{margin-left:23px;padding:0 31px 0 21px}
.nav .about{padding:0 25px 0 22px}
.nav .buyers{padding:0 28px 0 29px}
.nav .sellers{padding:0 29px 0 26px}
.nav .media{padding:0 30px 0 25px}
.nav .contact{padding:0 0 0 24px}
.hero{position:absolute;left:0;top:119px;width:1200px;height:374px;background:linear-gradient(180deg,#7fc0ea 0%,#b9def2 28%,#3f6e2a 45%,#3b6b24 62%,#b4a85a 72%,#a5b832 82%,#b7c93a 100%)}
.signup{position:absolute;left:141px;top:479px;width:922px;height:92px;background:linear-gradient(180deg,#e9e9e9 0%,#ffffff 75%);box-shadow:-8px 6px 10px -6px rgba(0,0,0,.25),8px 6px 10px -6px rgba(0,0,0,.25)}
.signup-label{position:absolute;left:31px;top:14px;font-family:"Tinos",serif;font-size:27px;color:#222}
.signup-input{position:absolute;left:317px;top:15px;width:414px;height:34px;border:1px solid #cfcfcf;background:#fff;font-style:italic;font-size:13px;color:#777;padding:9px 11px}
.signup-btn{position:absolute;left:730px;top:14px;width:120px;height:35px;background:linear-gradient(180deg,var(--green-top),var(--green-bot));color:#fff;font-family:"Source Sans 3",sans-serif;font-size:21px;text-align:center;line-height:34px}
.intro{position:absolute;left:102px;top:582px;width:700px}
.intro h1{font-family:"Source Sans 3",sans-serif;font-weight:600;font-size:23px;letter-spacing:1px;color:var(--gold);margin-bottom:7px}
.intro p{font-size:13px;line-height:18px;letter-spacing:.35px;text-align:justify;margin-bottom:20px}
.video{position:absolute;left:824px;top:585px;width:274px;height:213px;background:radial-gradient(ellipse at 50% 45%,#2b2b2b 0%,#0d0d0d 75%)}
.video-controls{position:absolute;left:5px;top:187px;width:264px;height:20px;background:#e9e9e9;font-size:9px;font-weight:700;color:#111}
.band{position:absolute;left:0;top:822px;width:1200px;height:250px;background:var(--beige)}
.tab{position:absolute;height:44px;font-family:"Source Sans 3",sans-serif;font-size:21px;letter-spacing:1px;line-height:44px;border-radius:6px 6px 0 0}
.tab-featured{left:102px;top:20px;width:203px;background:#fff;text-align:center;color:#111;border:1px solid #e6e0cc;border-bottom:none}
.tab-upcoming{left:325px;top:20px;width:213px;background:#e4d6a8;text-align:center;color:#2a2620;border:1px solid #c9b887}
.auction-panel{position:absolute;left:101px;top:63px;width:674px;height:160px;background:#fff;border-radius:0 6px 6px 6px}
.auction-photo{position:absolute;left:10px;top:14px;width:234px;height:135px;background:linear-gradient(180deg,#8fa7bf 0%,#cfd3d3 40%,#8d8a7a 70%,#4a5a2e 100%)}
.auction-text{position:absolute;left:255px;top:15px;width:400px;font-size:13px;line-height:16px;letter-spacing:.4px;text-align:justify}
.click-btn{position:absolute;left:254px;top:123px;width:89px;height:23px;background:#262626;border-radius:5px;color:#fff;font-size:14px;line-height:22px;padding-left:7px}
.divider{position:absolute;left:794px;top:18px;height:215px;border-left:2px solid #d9d2bd}
.testimonials{position:absolute;left:816px;top:30px;width:280px}
.testimonials h2{font-family:"Source Sans 3",sans-serif;font-weight:400;font-size:21px;letter-spacing:1px;color:#111;margin-bottom:6px}
.testimonials p{font-size:13px;line-height:18px;letter-spacing:.4px;padding-left:2px}
.quote-mark{position:absolute;left:-14px;top:22px;font-family:"Tinos",serif;font-size:28px;color:var(--tan-dark)}
.footer{position:absolute;left:0;top:1072px;width:1200px;height:111px;background:var(--footer);color:#fff}
.footer-nav{position:absolute;left:112px;top:31px;font-size:13px;word-spacing:0}
.footer-nav span{margin:0 14px}
.footer-contact{position:absolute;left:112px;top:53px;font-size:13px}
.footer-copy{position:absolute;left:112px;top:75px;font-size:12px}
.badges{position:absolute;left:863px;top:24px}
</style>
</head>
<body>
<div class="top-stripe"></div>
<header class="header">
  <nav>
    <ul class="nav">
      <li class="home">Home</li>
      <li class="auctions">Auctions</li>
      <li class="about">About Us</li>
      <li class="buyers">Buyers</li>
      <li class="sellers">Sellers</li>
      <li class="media">Media</li>
      <li class="contact">Contact Us</li>
    </ul>
  </nav>
</header>
<div class="brand">
  <svg width="123" height="186" viewBox="0 0 123 186">
    <defs><linearGradient id="bannerFill" x1="0" y1="0" x2="0" y2="1"><stop offset="0" stop-color="#e3d7b0"/><stop offset="1" stop-color="#cdbd8e"/></linearGradient></defs>
    <path d="M0 0H123V118L61.5 186L0 118Z" fill="url(#bannerFill)"/>
  </svg>
  <div class="brand-name">Harvest Gate Auctions</div>
</div>
<div class="hero" role="img" aria-label="Farm scene with red barns, silos, trees and green crop fields under a blue sky"></div>

<section class="signup">
  <div class="signup-label">Steady Relay Email:</div>
  <div class="signup-input">Email Address</div>
  <div class="signup-btn">Sign Up</div>
</section>

<section class="intro">
  <h1>Harvest Gate Auctions</h1>
  <p>simply dummy text of the printing and typesetting industry. Lorem Ipsum has been the industry's standard dummy text ever since the 1500s, when an unknown printer took a galley of type and scrambled it to make a type specimen book. It has survived not only five centuries, but also the leap into electronic typesetting, remaining essentially unchanged. It was popularised in the 1960s with the release of Letraset sheets containing Lorem Ipsum passages, and more recently with desktop publishing software.</p>
  <p style="line-height:20px">simply dummy text of the printing and typesetting industry. Lorem Ipsum has been the industry's standard dummy text ever since the 1500s, when an unknown printer took a galley of type and scrambled it to make a type specimen book.</p>
</section>

<div class="video" role="img" aria-label="Company introduction video">
  <svg style="position:absolute;left:115px;top:68px" width="44" height="44" viewBox="0 0 44 44"><path d="M10 4L38 22L10 40Z" fill="#e8e8e8" opacity=".85"/></svg>
  <div class="video-controls">
    <svg style="position:absolute;left:6px;top:5px" width="10" height="10"><path d="M1 0L9 5L1 10Z" fill="#111"/></svg>
    <span style="position:absolute;left:27px;top:5px">00:00</span>
    <div style="position:absolute;left:57px;top:8px;width:112px;height:4px;background:#999"></div>
    <span style="position:absolute;left:176px;top:5px">00:00</span>
    <svg style="position:absolute;left:210px;top:5px" width="30" height="10"><path d="M0 3H3L6 0V10L3 7H0Z" fill="#111"/><path d="M10 4h1v2h-1zM13 3h1v4h-1zM16 2h1v6h-1zM19 1h1v8h-1zM22 0h1v10h-1zM25 0h1v10h-1z" fill="#444"/></svg>
    <svg style="position:absolute;left:248px;top:4px" width="11" height="11"><path d="M0 0h4M0 0v4M11 0h-4M11 0v4M0 11h4M0 11v-4M11 11h-4M11 11v-4" stroke="#111" stroke-width="2" fill="none"/></svg>
  </div>
</div>

<section class="band">
  <div class="tab tab-featured">Featured Auctions</div>
  <div class="tab tab-upcoming">Upcoming Auctions</div>
  <div class="auction-panel">
    <div class="auction-photo" role="img" aria-label="Two-storey suburban house at dusk with a for-sale sign on the lawn"></div>
    <p class="auction-text">simply dummy text of the printing and typesetting industry. Lorem Ipsum has been the industry's standard dummy text ever since the 1500s, when an unknown printer took a galley of type and scrambled it to make a type with the release of Letraset sheets containing Lorem Ipsum passages, and more recently-specimen book.</p>
    <div class="click-btn">Click here
      <svg width="10" height="8" viewBox="0 0 10 8"><path d="M0 0L5 4L0 8ZM5 0L10 4L5 8Z" fill="#fff"/></svg>
    </div>
  </div>
  <div class="divider"></div>
  <div class="testimonials">
    <h2>Client Testimonals</h2>
    <span class="quote-mark">&ldquo;</span>
    <p>simply dummy text of the printing and type-setting industry. Lorem Ipsum has been the industry's standard dummy text ever since the 1500s, when an unknown printer took a galley of type and has been the industry's standard dummy text ever since the 1500s, when an scrambled it to make.</p>
  </div>
</section>

<footer class="footer">
  <div class="footer-nav">Home<span>|</span>Auctions<span>|</span>About Us<span>|</span>Buyers<span>|</span>Sellers<span>|</span>Media<span>|</span>Contact Us</div>
  <div class="footer-contact">Phone: 555- 014-2290, Email: info@bidplainfield.example</div>
  <div class="footer-copy">Copyright (C) HarvestGateAuctions. 2013.&nbsp; All Rights Reserved</div>
  <svg class="badges" width="222" height="74" viewBox="0 0 222 74" role="img" aria-label="Association membership badges">
    <rect x="2" y="4" width="52" height="66" rx="6" fill="#8d9093"/>
    <rect x="84" y="2" width="52" height="68" rx="6" fill="#d4d5d6"/>
    <rect x="166" y="2" width="52" height="58" rx="6" fill="#e6e6e6"/>
  </svg>
</footer>
</body>
</html>
```